Realtor resource

This is a website that provides resources for Realtors and their customers (home buyers and sellers).

There are 5 pages that I need redesigned:

1. Homepage: https://brightkeyguide.example/
2. Support Page/Contact Us: https://brightkeyguide.example/contact-us/
3. Agent Dashboard - See attached screenshot
4. Real Estate Documents page - See attached screenshot
5. Real Estate Contract page - see attached screenshot

Target Market(s)

Real estate agents and their customers.

Industry/Entity Type

Real Estate

Number of Pages Required

5+ page

Requirements
Must have
• Please use a modern design and incorporate design with current logo.

```html
<!DOCTYPE html>
<html lang="en">
<head>
<meta charset="utf-8">
<title>BrightKey Guide – Home</title>
<link href="https://fonts.googleapis.com/css2?family=Poppins:wght@400;500;600&display=swap" rel="stylesheet">
<style>
  :root {
    --orange: #f7941d;
    --ink: #1c1c1c;
    --white: #ffffff;
    --panel: #000000;
    --hero-dark: #2c3a48;
    --hero-mid: #56687a;
    --hero-light: #7d8c99;
    --social-1: #3b5998;
    --social-2: #1da1f2;
    --social-3: #0e76a8;
  }
  * { box-sizing: border-box; margin: 0; padding: 0; }
  html, body { width: 1200px; height: 568px; overflow: hidden; background: var(--white); }
  body { font-family: "Poppins", sans-serif; color: var(--ink); position: relative; }
  a { text-decoration: none; color: inherit; }

  .site-header { position: absolute; top: 0; left: 0; width: 1200px; height: 68px; }
  .brand { position: absolute; left: 140px; top: 16px; display: flex; align-items: center; gap: 8px; }
  .brand-name { font-size: 26px; font-weight: 500; color: var(--ink); letter-spacing: -0.5px; line-height: 36px; }
  .brand-dot { width: 30px; height: 30px; border-radius: 50%; background: var(--orange); }

  .main-nav a { position: absolute; top: 25px; font-size: 13px; color: var(--ink); line-height: 18px; }
  .main-nav .active { color: var(--orange); font-weight: 500; }
  .login-icon { position: absolute; left: 954px; top: 20px; width: 30px; height: 30px; border-radius: 50%; background: var(--orange); }

  .hero { position: absolute; top: 68px; left: 0; width: 1200px; height: 387px; }
  .hero-photo { position: absolute; inset: 0;
    background: radial-gradient(ellipse at 50% 55%, var(--hero-light) 0%, var(--hero-mid) 45%, var(--hero-dark) 100%); }
  .hero-title { position: absolute; top: 96px; width: 100%; text-align: center; color: var(--white);
    font-size: 28px; font-weight: 600; line-height: 45px; text-shadow: 0 2px 6px rgba(0,0,0,.6); }

  .audience { position: absolute; top: 211px; height: 73px; width: 301px; background: var(--panel);
    color: var(--white); font-weight: 600; }
  .audience.agent { left: 292px; border-radius: 6px 0 0 6px; }
  .audience.clients { left: 598px; border-radius: 0 6px 6px 0; }
  .audience-label { position: absolute; top: 50%; transform: translateY(-50%); font-size: 21px; white-space: nowrap; }
  .agent .audience-label { left: 12px; }
  .clients .audience-label { left: 100px; }
  .audience-icon { position: absolute; top: 6px; width: 61px; height: 61px; }
  .agent .audience-icon { left: 236px; }
  .clients .audience-icon { left: 18px; }

  .site-footer { position: absolute; top: 455px; left: 0; width: 1200px; height: 113px; }
  .follow { position: absolute; top: 42px; left: 505px; display: flex; align-items: center; font-size: 13px; }
  .social { display: flex; gap: 10px; margin-left: 12px; }
  .social span { width: 26px; height: 26px; border-radius: 50%; border: 2px solid #cfd8e0; }
  .social .s1 { background: var(--social-1); }
  .social .s2 { background: var(--social-2); }
  .social .s3 { background: var(--social-3); }
  .copyright { position: absolute; top: 78px; width: 100%; text-align: center; font-size: 13px; }
  .footer-bar { position: absolute; bottom: 0; left: 0; width: 1200px; height: 3px; background: var(--orange); }
</style>
</head>
<body>
  <header class="site-header">
    <a class="brand" href="https://brightkeyguide.example/">
      <span class="brand-name">BrightKey Guide</span>
      <span class="brand-dot"></span>
    </a>
    <nav class="main-nav">
      <a class="active" href="https://brightkeyguide.example/" style="left:558px">Home</a>
      <a href="#" style="left:619px">Support</a>
      <a href="#" style="left:693px">Real Estate Documents</a>
      <a href="https://brightkeyguide.example/contact-us/" style="left:863px;top:24px">Contact Us</a>
      <span class="login-icon">
        <svg width="30" height="30" viewBox="0 0 30 30" fill="none" stroke="#fff" stroke-width="1.6" stroke-linecap="round">
          <path d="M12 9.5a7 7 0 1 1 0 11"/><path d="M8 15h10M14.5 11.5 18 15l-3.5 3.5"/>
        </svg>
      </span>
      <a href="#" style="left:992px">Login Here</a>
    </nav>
  </header>

  <section class="hero">
    <div class="hero-photo" role="img" aria-label="Blurred photo of business professionals reviewing papers in front of a city skyline window"></div>
    <h1 class="hero-title">Real Estate Contracts Explained In Plain Language<br>By Texas Real Estate Attorneys</h1>

    <a class="audience agent" href="#">
      <span class="audience-label">Real Estate Agent</span>
      <svg class="audience-icon" viewBox="0 0 61 61">
        <circle cx="30.5" cy="30.5" r="30.5" fill="var(--orange)"/>
        <circle cx="30.5" cy="30.5" r="27" fill="none" stroke="#fff" stroke-width="1" stroke-dasharray="1.5 2.5"/>
        <path d="M19 31 30.5 21 42 31M22 29v11h17V29M28 40v-6h5v6" fill="none" stroke="#fff" stroke-width="1.8" stroke-linejoin="round"/>
      </svg>
    </a>

    <a class="audience clients" href="#">
      <svg class="audience-icon" viewBox="0 0 61 61">
        <circle cx="30.5" cy="30.5" r="30.5" fill="var(--orange)"/>
        <circle cx="30.5" cy="30.5" r="27" fill="none" stroke="#fff" stroke-width="1" stroke-dasharray="1.5 2.5"/>
        <path d="M19 31 30.5 21 42 31M22 29v11h17V29M28 40v-6h5v6" fill="none" stroke="#fff" stroke-width="1.8" stroke-linejoin="round"/>
      </svg>
      <span class="audience-label">Buyers &amp; Sellers</span>
    </a>
  </section>

  <footer class="site-footer">
    <div class="follow">Follow Us On
      <div class="social"><span class="s1"></span><span class="s2"></span><span class="s3"></span></div>
    </div>
    <p class="copyright">Copyright © 2019 BrightKey Guide.&nbsp; All Rights Reserved.</p>
    <div class="footer-bar"></div>
  </footer>
</body>
</html>
```